Plakat-Design für Bauunternehmung
Zielgruppe
Wir sind eine Bauunternehmung (Meisterbetrieb und Ingenieurbüro) welche Erd- Maurer- und Betonarbeiten anbietet. Unser Fokus liegt auf Professionalität und qualitativ einwandfreie Arbeit. Wir sind teuer aber die besten in dem was wir machen. Unsere Zielgruppe liegt bei Kunden welche eine qualitativ einwandfreie Arbeit erwarten und bewusst sind dass das auch Geld kostet. Unserem Kunden ist die Geldfrage immer zweitrangig und er legt viel mehr wert auf andere Faktoren: Qualität, Zuverlässigkeit, Qualifikation, Termineinhaltung etc. Es ist selbstverständlich das die Kunden meist vermögender sind.
Aufgabenstellung
Format: 340 x 175 cm
Was muss drauf:
- Logo
- Firmendaten:
Lindmoosweg 7, 89079 Ulm
Telefon: +49 (0) 7305 - 4418273
Mobil: +49 (0) 176 - 20394857
E-Mail: mortek@beispielpost.de
- Zusätzliche Informationen: Es sollte irgendwo noch 'Bauunternehmung' stehen, es sollte etwas größer sein, unter Logo oder ähnlich, Es muss klar sein das wir eine Bauunternehmung sind. Zusätzlich dazu noch unsere Leistungen 'Neubau, Umbau, Anbau', nebeneinander oder übereinander ist euch überlassen.

```html
<!DOCTYPE html>
<html lang="de">
<head>
<meta charset="utf-8">
<title>mortek – Bauunternehmung Banner</title>
<link rel="stylesheet" href="https://fonts.googleapis.com/css2?family=Montserrat:wght@500;600;700&family=Source+Sans+3:wght@500;600&display=swap">
<style>
  :root {
    --page-bg: #d6d6d6;
    --dark-light: #434446;
    --dark-deep: #242527;
    --white: #f3f3f3;
    --ink: #1b1b1c;
    --ribbon-black: #0c0c0c;
    --ribbon-gold: #c9a72e;
  }
  * { box-sizing: border-box; margin: 0; padding: 0; }
  html, body {
    width: 857px; height: 1200px; overflow: hidden;
    background: var(--page-bg);
  }
  .sheet {
    width: 857px; height: 1200px;
    display: flex; flex-direction: column;
    align-items: center; justify-content: space-evenly;
  }
  .banner {
    position: relative;
    width: 680px; height: 350px;
    background: var(--white);
    overflow: hidden;
  }
  .banner__field {
    position: absolute; left: 0; top: 0;
    width: 100%; height: 280px;
    background: radial-gradient(ellipse at 22% 30%, var(--dark-light) 0%, var(--dark-deep) 70%);
    color: var(--white);
  }
  .brand {
    position: absolute; left: 164px; top: 22px;
    display: flex; align-items: flex-end; gap: 18px;
  }
  .brand__square {
    width: 78px; height: 78px; background: var(--white);
  }
  .brand__text { position: relative; }
  .brand__claim {
    font-family: "Montserrat", sans-serif; font-weight: 500;
    font-size: 10.5px; letter-spacing: 0.2px;
    position: absolute; right: 0; top: -6px; white-space: nowrap;
  }
  .brand__name {
    font-family: "Montserrat", sans-serif; font-weight: 700;
    font-size: 68px; line-height: 1; letter-spacing: -1px;
    display: block; padding-top: 12px; margin-bottom: -10px;
  }
  .headline {
    position: absolute; left: 0; right: 0; top: 128px;
    text-align: center;
    font-family: "Montserrat", sans-serif; font-weight: 700;
    font-size: 52px; line-height: 1; letter-spacing: 0.3px;
  }
  .services {
    position: absolute; left: 0; right: 0; top: 190px;
    text-align: center;
    font-family: "Montserrat", sans-serif; font-weight: 600;
    font-size: 33px; line-height: 1; letter-spacing: 0.5px;
  }
  .address {
    position: absolute; left: 185px; top: 263px;
    width: 310px; height: 34px;
    clip-path: polygon(4% 0, 96% 0, 100% 50%, 96% 100%, 4% 100%, 0 50%);
    display: flex; align-items: center; justify-content: center;
    font-family: "Source Sans 3", sans-serif; font-weight: 600;
    font-size: 19px; color: var(--white);
  }
  .address--black { background: var(--ribbon-black); }
  .address--gold { background: var(--ribbon-gold); }
  .contacts {
    position: absolute; left: 0; right: 0; top: 305px;
    display: flex; justify-content: center; gap: 16px;
    font-family: "Source Sans 3", sans-serif; font-weight: 500;
    font-size: 18px; color: var(--ink);
  }
  .contact { display: flex; align-items: center; gap: 5px; white-space: nowrap; }
  .contact svg { fill: var(--ink); }
  .contact--mail { font-weight: 600; margin-left: 6px; }
</style>
</head>
<body>
<main class="sheet">

  <section class="banner" aria-label="Banner, Variante schwarz">
    <div class="banner__field">
      <div class="brand">
        <span class="brand__square"></span>
        <span class="brand__text">
          <span class="brand__claim">MEISTERBETRIEB &amp; INGENIEURBÜRO</span>
          <span class="brand__name">mortek</span>
        </span>
      </div>
      <h1 class="headline">Bauunternehmung</h1>
      <p class="services">Neubau - Umbau - Anbau</p>
    </div>
    <div class="address address--black">Lindmoosweg 7, 89079 Ulm</div>
    <div class="contacts">
      <span class="contact"><svg width="15" height="15" viewBox="0 0 24 24"><path d="M6.6 10.8a15 15 0 0 0 6.6 6.6l2.2-2.2a1 1 0 0 1 1-.25 11.4 11.4 0 0 0 3.6.6 1 1 0 0 1 1 1V20a1 1 0 0 1-1 1A17 17 0 0 1 3 4a1 1 0 0 1 1-1h3.5a1 1 0 0 1 1 1c0 1.25.2 2.45.6 3.6a1 1 0 0 1-.25 1z"/></svg>+49 (0) 7305 - 4418273</span>
      <span class="contact"><svg width="10" height="17" viewBox="0 0 10 17"><path d="M1.5 0h7A1.5 1.5 0 0 1 10 1.5v14A1.5 1.5 0 0 1 8.5 17h-7A1.5 1.5 0 0 1 0 15.5v-14A1.5 1.5 0 0 1 1.5 0zm.2 2v12.5h6.6V2z"/></svg>+49 (0) 176 - 20394857</span>
      <span class="contact contact--mail"><svg width="16" height="11" viewBox="0 0 16 11"><path d="M0 0h16v1.5L8 6 0 1.5zM0 3.2l8 4.5 8-4.5V11H0z"/></svg>mortek@beispielpost.de</span>
    </div>
  </section>

  <section class="banner" aria-label="Banner, Variante gold">
    <div class="banner__field">
      <div class="brand">
        <span class="brand__square"></span>
        <span class="brand__text">
          <span class="brand__claim">MEISTERBETRIEB &amp; INGENIEURBÜRO</span>
          <span class="brand__name">mortek</span>
        </span>
      </div>
      <h2 class="headline">Bauunternehmung</h2>
      <p class="services">Neubau - Umbau - Anbau</p>
    </div>
    <div class="address address--gold">Lindmoosweg 7, 89079 Ulm</div>
    <div class="contacts">
      <span class="contact"><svg width="15" height="15" viewBox="0 0 24 24"><path d="M6.6 10.8a15 15 0 0 0 6.6 6.6l2.2-2.2a1 1 0 0 1 1-.25 11.4 11.4 0 0 0 3.6.6 1 1 0 0 1 1 1V20a1 1 0 0 1-1 1A17 17 0 0 1 3 4a1 1 0 0 1 1-1h3.5a1 1 0 0 1 1 1c0 1.25.2 2.45.6 3.6a1 1 0 0 1-.25 1z"/></svg>+49 (0) 7305 - 4418273</span>
      <span class="contact"><svg width="10" height="17" viewBox="0 0 10 17"><path d="M1.5 0h7A1.5 1.5 0 0 1 10 1.5v14A1.5 1.5 0 0 1 8.5 17h-7A1.5 1.5 0 0 1 0 15.5v-14A1.5 1.5 0 0 1 1.5 0zm.2 2v12.5h6.6V2z"/></svg>+49 (0) 176 - 20394857</span>
      <span class="contact contact--mail"><svg width="16" height="11" viewBox="0 0 16 11"><path d="M0 0h16v1.5L8 6 0 1.5zM0 3.2l8 4.5 8-4.5V11H0z"/></svg>mortek@beispielpost.de</span>
    </div>
  </section>

</main>
</body>
</html>
```